Eye Doctor Needs Updated Business Card

We need a standard US business card designed for an optometrist's practice. Our practice name is Hollen Sight Clinic and attached you'll find our logos. We are located in a smaller community, we are a trusted source for eye care and designer eyewear. We have 2 different version of our logos, so both versions are attached. Our slogan is "Close to Home, Clear in Focus". I'd like to see designs with one of our logos on the front with our contact info, and have the slogan on the back by itself. Final design should be professional looking, include the colors of our logo or colors that compliment the logo. We want it to look appropriate for a healthcare practice but also up-to-date, eye-catching, to have the normal contact info like address, phone #, email, but also possibly room for additional contact info such as facebook.
Updates

I just uploaded .eps files to use instead of the jpeg. Hope that helps!

So many great designs! We tending to like the darker blues that are used in our logo as the main blue color for the business cards. We also really like the use of a water-mark type appearance on either the front and/or back, or the embossed look as well looks nice. Thank you all for such great designs!

We're preferring the designs where white and the darker blue used in our logo are the primary colors on the front, but with a little green used as well. Again though, thanks for all the impressive designs so far!

Industry/Entity Type

Healthcare

```html
<!DOCTYPE html>
<html lang="en">
<head>
<meta charset="utf-8">
<title>Hollen Sight Clinic – Business Card</title>
<link rel="stylesheet" href="https://fonts.googleapis.com/css2?family=Bitter:wght@400;600&display=swap">
<style>
  :root {
    --stage: #e9e7e4;
    --white: #ffffff;
    --navy: #1c4f86;
    --blue-deep: #1f5fa3;
    --blue-light: #4fb8ea;
    --green: #5cb82e;
    --green-bright: #48e80c;
    --green-deep: #2f9a12;
    --ink-light: #ffffff;
  }
  * { margin: 0; padding: 0; box-sizing: border-box; }
  html, body { width: 1200px; height: 442px; overflow: hidden; }
  body {
    background: var(--stage);
    font-family: "Bitter", Georgia, serif;
    position: relative;
  }
  .card {
    position: absolute;
    top: 66px;
    width: 540px;
    height: 309px;
    overflow: hidden;
    box-shadow: 0 6px 18px rgba(0,0,0,0.25);
  }
  .card--front { left: 40px; background: var(--white); }
  .card--back {
    left: 620px;
    background: radial-gradient(ellipse at 45% 55%, var(--green-bright) 0%, #3cc810 45%, var(--green-deep) 100%);
  }
  .front-art { position: absolute; inset: 0; }

  .brand {
    position: absolute;
    left: 24px;
    top: 118px;
    width: 210px;
    display: flex;
    flex-direction: column;
    align-items: center;
    gap: 14px;
  }
  .brand__dot {
    width: 54px; height: 54px;
    border-radius: 50%;
    background: var(--navy);
  }
  .brand__name {
    font-weight: 600;
    font-size: 22px;
    color: var(--navy);
    text-align: center;
    line-height: 1.1;
  }

  .contact {
    position: absolute;
    right: 26px;
    top: 30px;
    text-align: right;
    color: var(--ink-light);
  }
  .contact__name { font-size: 19px; line-height: 1.1; }
  .contact__title { font-size: 12px; margin-bottom: 34px; }
  .contact__list { list-style: none; font-size: 13.5px; line-height: 1.5; }
  .contact__list li { display: flex; justify-content: flex-end; align-items: center; gap: 5px; }
  .contact__list svg { width: 11px; height: 11px; flex: none; }
  .contact__address { margin-top: 22px; font-size: 13.5px; line-height: 1.5; }

  .back-mark {
    position: absolute;
    right: -20px;
    top: 10px;
    width: 290px; height: 290px;
    border-radius: 50%;
    border: 2px solid rgba(255,255,255,0.18);
    background: rgba(255,255,255,0.06);
  }
  .back-brand {
    position: absolute;
    left: 24px;
    top: 128px;
    width: 230px;
    text-align: center;
    color: var(--ink-light);
  }
  .back-brand__name { font-weight: 600; font-size: 25px; white-space: nowrap; }
  .back-brand__slogan {
    margin-top: 12px;
    font-size: 15.5px;
    line-height: 1.35;
  }
</style>
</head>
<body>

<section class="card card--front">
  <svg class="front-art" viewBox="0 0 540 309" aria-hidden="true">
    <defs>
      <linearGradient id="blueBand" x1="0" y1="0" x2="1" y2="0">
        <stop offset="0" stop-color="var(--blue-deep)"/>
        <stop offset="1" stop-color="var(--blue-light)"/>
      </linearGradient>
    </defs>
    <path d="M300,0 C250,80 238,190 268,309 L540,309 L540,0 Z" fill="url(#blueBand)"/>
    <path d="M285,0 C236,80 222,190 254,309" fill="none" stroke="var(--green)" stroke-width="4"/>
  </svg>

  <div class="brand">
    <span class="brand__dot"></span>
    <span class="brand__name">Hollen Sight Clinic</span>
  </div>

  <div class="contact">
    <p class="contact__name">Your Name</p>
    <p class="contact__title">Title</p>
    <ul class="contact__list">
      <li><svg viewBox="0 0 10 10"><rect width="10" height="10" rx="1.5" fill="#3b5ba8"/></svg>/hollensight.com</li>
      <li><svg viewBox="0 0 10 10"><path d="M2,1 L4,1 L4.6,3 L3.4,4 C4,5.4 4.8,6.2 6,6.6 L7,5.4 L9,6 L9,8 C5,9 1,5 2,1 Z" fill="#fff"/></svg>123-456-7890</li>
      <li><svg viewBox="0 0 10 10"><rect x="0.5" y="2" width="9" height="6" fill="none" stroke="#fff"/><path d="M0.5,2 L5,5.5 L9.5,2" fill="none" stroke="#fff"/></svg>hello@hollensight.com</li>
      <li><svg viewBox="0 0 10 10"><circle cx="5" cy="5" r="4.3" fill="none" stroke="#fff" stroke-width="0.9"/><path d="M0.7,5 H9.3 M5,0.7 V9.3" stroke="#fff" stroke-width="0.7"/></svg>www.hollensight.com</li>
    </ul>
    <p class="contact__address">Street Name, City Name<br>State Zipcode</p>
  </div>
</section>

<section class="card card--back">
  <span class="back-mark"></span>
  <div class="back-brand">
    <p class="back-brand__name">Hollen Sight Clinic</p>
    <p class="back-brand__slogan">Close to Home,<br>Clear in Focus</p>
  </div>
</section>

</body>
</html>
```